Postcard 1st Design

The place is called Fen-O-Lark Hall. It's in the county between the cities of Dunmere & Halvaston, hence the name of the area. It had been a bar w/food for 50 years but was closed for 5yrs. It's all cleaned up, remodeled & raring to go. The bar opened in February and has had live music with no cover charge every week-end. Now the kitchen side (Called PaPa J's PIZZA & PASTA) opened Nov 1st. We have already owned the family restaurant right next door - called Ms. T's Family Restaurant for 16 years. Ms. T's is wildly successful, but sells no Italian food whatsoever, so the PaPa J's of us is opening right next door as competition. However, only 1 pizza competitor is in our area of about 3500 people. We would like for you to design 3 postcards as coupons. We are going to send a first mailing to about 400 homes. The 2nd card they rec. will depend on whether or not they used the first one. Get it? I have made over 20 TV commercials, if you would like to watch a sample of my advertising humor, go to our website, mstsfamilydiner.example. The drift is this is a NEW Pizza place called PaPa J's located inside Fen-O-Lark Hall. Folks in this small neck of the woods will get the drift that the two places are related, and we're trying to draw off the goodwill of the name Ms. T's. So far as the first postcard should offer a $5.00 coupon for Ms. T's for buying ANY pizza at PaPa J's.

```html
<!DOCTYPE html>
<html lang="en">
<head>
<meta charset="utf-8">
<title>PaPa J's Pizza &amp; Pasta – Postcard</title>
<link rel="stylesheet" href="https://fonts.googleapis.com/css2?family=Alfa+Slab+One&family=Handlee&family=Open+Sans:ital,wght@0,600;0,700;1,700&family=Oswald:wght@300;400;600;700&display=swap">
<style>
  :root {
    --maroon: #8c1d2b;
    --red: #c8202a;
    --green: #2ea34a;
    --cream: #fbf1d9;
    --tan: #e8d3ae;
    --dark: #2b2321;
    --white: #ffffff;
    --stamp: #b3b3b5;
    --stage: #efeae3;
  }
  * { margin: 0; padding: 0; box-sizing: border-box; }
  html, body { width: 1200px; height: 500px; overflow: hidden; }
  body { background: var(--stage); position: relative; font-family: "Oswald", sans-serif; }

  .card { position: absolute; top: 33px; height: 432px; overflow: hidden; }
  .card--front { left: 33px; width: 559px; background: var(--cream); }
  .card--back { left: 612px; width: 561px; background: var(--white); }

  /* Wordmark: one colour, one weight of the text font */
  .wordmark { position: absolute; font-family: "Oswald", sans-serif; font-weight: 700; color: var(--dark); white-space: nowrap; text-transform: uppercase; letter-spacing: 1px; }
  .front__brand { left: 22px; top: 6px; font-size: 50px; line-height: 64px; }
  .front__new { position: absolute; left: 318px; top: 8px; font-family: "Open Sans", sans-serif; font-weight: 700; font-style: italic; font-size: 22px; color: var(--red); }
  .front__kind { position: absolute; left: 312px; top: 38px; font-family: "Open Sans", sans-serif; font-weight: 600; font-size: 29px; line-height: 36px; color: var(--dark); letter-spacing: .5px; }
  .ppp-band { position: absolute; left: 0; top: 76px; width: 100%; height: 30px; background: var(--green); }
  .ppp-band__text { position: absolute; left: 150px; top: 0; font-family: "Handlee", cursive; font-size: 21px; line-height: 30px; color: var(--cream); }
  .front__headline { position: absolute; left: 0; top: 108px; width: 100%; text-align: center; font-family: "Alfa Slab One", serif; font-weight: 400; font-size: 37px; line-height: 48px; color: var(--maroon); }
  .front__photo { position: absolute; left: 0; top: 157px; width: 100%; height: 238px;
    background: radial-gradient(ellipse at 45% 55%, #f2d27a 0%, #e3a651 35%, #b8552d 65%, #6e3a22 100%); }
  .front__footer { position: absolute; left: 0; bottom: 0; width: 100%; height: 70px; }
  .front__contact { position: absolute; left: 0; bottom: 12px; width: 100%; text-align: center; color: var(--white); font-size: 16px; font-weight: 400; letter-spacing: .2px; }

  .venue-badge { position: absolute; left: 25px; top: 264px; width: 110px; height: 106px; background: var(--red); }
  .venue-badge__label { display: block; text-align: center; color: var(--white); font-family: "Open Sans", sans-serif; font-weight: 700; font-size: 13px; line-height: 15px; padding-top: 4px; }
  .venue-badge__name { position: absolute; left: 6px; right: 6px; bottom: 6px; height: 62px; background: var(--dark); color: var(--white);
    font-weight: 600; font-size: 17px; line-height: 20px; display: flex; align-items: center; justify-content: center; text-align: center; }

  .coupon { position: absolute; left: 355px; top: 190px; width: 197px; height: 202px; background: var(--cream); padding: 5px; }
  .coupon__inner { width: 100%; height: 100%; border: 2px dashed var(--maroon); text-align: center; padding-top: 8px; }
  .coupon__amount { font-size: 46px; font-weight: 700; line-height: 50px; color: var(--green); }
  .coupon__amount sup { font-size: 24px; vertical-align: 16px; }
  .coupon__where { font-weight: 700; color: var(--maroon); font-size: 28px; line-height: 34px; }
  .coupon__terms { font-family: "Open Sans", sans-serif; font-weight: 600; font-size: 19px; line-height: 22px; color: var(--dark); }
  .coupon__brand { font-weight: 700; color: var(--dark); font-size: 26px; line-height: 34px; text-transform: uppercase; letter-spacing: 1px; }

  /* Back */
  .back__about { position: absolute; left: 0; top: 0; width: 282px; height: 312px; background: linear-gradient(180deg, var(--cream) 0%, #f3e3c4 60%, var(--tan) 100%); }
  .ribbon { position: absolute; left: 22px; top: 19px; height: 24px; display: flex; }
  .ribbon__flag { width: 12px; background: var(--green); }
  .ribbon__title { background: var(--white); padding: 0 8px; font-family: "Oswald", sans-serif; font-weight: 400; font-size: 14px; line-height: 24px; color: var(--dark); }
  .ribbon__tail { width: 12px; background: var(--maroon); clip-path: polygon(0 0, 100% 0, 60% 50%, 100% 100%, 0 100%); }
  .about__heading { position: absolute; left: 30px; top: 47px; width: 232px; font-weight: 700; font-size: 18px; line-height: 22px; color: var(--red); letter-spacing: .3px; }
  .about__list { position: absolute; left: 30px; top: 99px; list-style: none; font-weight: 400; font-size: 13px; line-height: 20px; color: var(--dark); }
  .about__list li::before { content: ""; display: inline-block; width: 6px; height: 6px; border-radius: 50%; background: var(--maroon); margin-right: 7px; vertical-align: 2px; }
  .about__ppp { position: absolute; left: 0; top: 164px; width: 282px; height: 28px; background: linear-gradient(90deg, rgba(200,160,110,.15), rgba(190,145,95,.6)); font-family: "Handlee", cursive; font-size: 20px; line-height: 28px; color: var(--green); padding-left: 26px; }
  .about__icon { position: absolute; left: 38px; top: 200px; width: 36px; height: 36px; border-radius: 50%; background: radial-gradient(circle, #e8a84a, #7a3f8c); }
  .about__hours { position: absolute; left: 78px; top: 204px; font-weight: 600; font-size: 14px; line-height: 19px; color: var(--red); }
  .about__cta { position: absolute; left: 0; top: 253px; width: 282px; text-align: center; color: var(--dark); font-size: 13px; line-height: 19px; font-weight: 300; }
  .about__cta strong { font-weight: 600; font-size: 14px; }
  .back__band { position: absolute; left: 0; top: 312px; width: 100%; height: 52px; background: var(--green); color: var(--white); text-align: center; font-weight: 700; font-size: 22px; line-height: 52px; letter-spacing: .5px; }
  .back__band svg, .front__contact svg { vertical-align: -2px; margin-right: 6px; }
  .back__brand { left: 330px; top: 12px; width: 150px; text-align: center; font-size: 30px; line-height: 40px; }
  .back__kind { position: absolute; left: 330px; top: 51px; width: 150px; text-align: center; font-family: "Open Sans", sans-serif; font-weight: 600; font-size: 14px; color: var(--dark); }
  .back__address { position: absolute; left: 330px; top: 72px; width: 150px; text-align: center; font-size: 13px; line-height: 18px; font-weight: 300; color: var(--dark); }
  .stamp { position: absolute; left: 495px; top: 19px; width: 56px; height: 60px; background: var(--stamp); }
</style>
</head>
<body>

<section class="card card--front" aria-label="Postcard front">
  <div class="wordmark front__brand">PaPa J's</div>
  <div class="front__new">New Pizza Place!</div>
  <div class="front__kind">PIZZA &amp; PASTA</div>
  <div class="ppp-band"><span class="ppp-band__text">PPP (Pizza, Pasta &amp; Pub)</span></div>
  <h1 class="front__headline">Crust us, it’s so good!</h1>
  <div class="front__photo" role="img" aria-label="Photo of a pepperoni, olive and mushroom pizza with a slice being lifted"></div>

  <svg class="front__footer" viewBox="0 0 559 70" preserveAspectRatio="none" aria-hidden="true">
    <path d="M0 18 Q280 -6 559 18 L559 70 L0 70 Z" fill="var(--green)"/>
  </svg>
  <p class="front__contact">
    <svg width="14" height="14" viewBox="0 0 24 24" aria-hidden="true"><circle cx="12" cy="12" r="11" fill="none" stroke="#fff" stroke-width="2"/><path d="M8 6c-1 1-1 3 1 6s4 5 6 5l1-2-2-2-1 1c-1-.5-3-2.5-3.5-3.5l1-1-2-2z" fill="#fff"/></svg>555.014.2290 | 2187 W. Lantern Street, in beautiful Dunmere, IL
  </p>

  <div class="venue-badge">
    <span class="venue-badge__label">LOCATED<br>INSIDE</span>
    <span class="venue-badge__name">Fen-O-Lark<br>Hall</span>
  </div>

  <div class="coupon">
    <div class="coupon__inner">
      <div class="coupon__amount"><sup>$</sup>5 OFF</div>
      <div class="coupon__where">Ms. T's</div>
      <div class="coupon__terms">for buying<br>ANY pizza at</div>
      <div class="coupon__brand">PaPa J's</div>
    </div>
  </div>
</section>

<section class="card card--back" aria-label="Postcard back">
  <div class="back__about">
    <div class="ribbon">
      <span class="ribbon__flag"></span>
      <span class="ribbon__title">About PaPa J's Pizza &amp; Pasta</span>
      <span class="ribbon__tail"></span>
    </div>
    <h2 class="about__heading">A new Pizza place located inside Fen-O-Lark Hall.</h2>
    <ul class="about__list">
      <li>Full bar with live shows on Saturdays</li>
      <li>Pool, Darts, and video gaming</li>
      <li>Daily drink specials</li>
    </ul>
    <div class="about__ppp">PPP (Pizza, Pasta &amp; Pub)</div>
    <div class="about__icon" role="img" aria-label="Small illustration of pasta and pizza"></div>
    <p class="about__hours">Pizza &amp; Pasta Served Daily<br>From 10:00 AM to 10:00 PM</p>
    <p class="about__cta"><strong>Pick up our Homemade Pizza Today.</strong><br>Or Come In and Observe Us<br>While We Make It.</p>
  </div>

  <div class="wordmark back__brand">PaPa J's</div>
  <div class="back__kind">PIZZA &amp; PASTA</div>
  <p class="back__address">2187 W. Lantern St.<br>Dunmere, IL</p>
  <div class="stamp" aria-hidden="true"></div>

  <div class="back__band">
    <svg width="18" height="18" viewBox="0 0 24 24" aria-hidden="true"><circle cx="12" cy="12" r="11" fill="none" stroke="#fff" stroke-width="2"/><path d="M8 6c-1 1-1 3 1 6s4 5 6 5l1-2-2-2-1 1c-1-.5-3-2.5-3.5-3.5l1-1-2-2z" fill="#fff"/></svg>555.014.2290
  </div>
</section>

</body>
</html>
```